New UK IT business
Business cards etc
Project: New UK IT business
New UK IT business - Environment
Creative Brief
Bright & Fun-filled
Cobalt Harvest Limited or Ltd - Gordon Pressey
Director
14 Brindle Lane Oakhurst Trading Park Fenwick Cross Herts HP9 3QL United Kingdom
gord@cobaltharvest-example.com
www.cobaltharvest-example.com
please do one card for Gord Pressey - Director and one for Rosalind Pressey - Director and one for Company - with no name
full colour - simple logo and website address only for the inside of the card i want it to have the fold on the horizontal meaning 55mm down the front with logo and name and address details the back as described above the inside I would like a picture of business people and have the messages of Redundant IT and Computer equipment Business people - corporate business people wanted All UK areas please suggest what you think and design around it thanks I will be available to answer questions when i see some designs for inspiration

```html
<!DOCTYPE html>
<html lang="en">
<head>
<meta charset="utf-8">
<title>Cobalt Harvest – Stationery Set</title>
<link href="https://fonts.googleapis.com/css2?family=Arimo:wght@400;700&display=swap" rel="stylesheet">
<style>
:root{
  --green:#3c9b2b;
  --green-light:#8cc63f;
  --green-dark:#1f6b1a;
  --paper:#ffffff;
  --edge:#d9d9d9;
  --ink:#3a3a3a;
  --muted:#666;
  --faint:#eef2ec;
  --photo-top:#e8efe1;
  --photo-mid:#b9c9a6;
  --photo-low:#6f9a55;
}
*{box-sizing:border-box;margin:0;padding:0}
html,body{width:1200px;height:360px;overflow:hidden;background:#fff}
body{position:relative;font-family:"Arimo",Arial,sans-serif;color:var(--ink)}
.piece{position:absolute;background:var(--paper);border:1px solid var(--edge);box-shadow:0 1px 3px rgba(0,0,0,.15);overflow:hidden}
.wave{position:absolute;left:0;bottom:0;width:100%;display:block}
.brand{position:absolute;display:flex;align-items:center;gap:4px;font-weight:700;color:var(--green);white-space:nowrap;line-height:1}
.brand-dot{border-radius:50%;background:currentColor;flex:none}
.photo{position:absolute;left:0;top:0;width:100%;background:linear-gradient(180deg,var(--photo-top) 0%,var(--photo-mid) 55%,var(--photo-low) 100%)}
.seal{position:absolute;border-radius:50%;background:var(--faint)}
.address{position:absolute;right:10px;top:12px;width:92px;text-align:right;font-size:5px;line-height:1.4;color:var(--muted)}
.footer-url{position:absolute;left:0;right:0;bottom:4px;text-align:center;font-size:5px;color:#fff}
.card-text{position:absolute;left:0;right:0;text-align:center;color:#fff;line-height:1.3}
.doc-title{position:absolute;left:14px;top:52px;font-weight:700;color:var(--green-dark)}
.field{display:flex;gap:4px;align-items:center;font-size:5px;margin-bottom:3px}
.field span{width:26px}
.field i{flex:1;height:5px;background:#e3e3e3}
.fax-box{display:inline-block;width:22px;height:6px;background:var(--green-light);margin:1px}
table{border-collapse:collapse;width:100%;font-size:4.5px}
th{background:var(--green);color:#fff;text-align:left;padding:2px}
td{border-bottom:1px solid #e6e6e6;height:7px}
</style>
</head>
<body>

<!-- folded card: inside with message (upside down) and front -->
<div class="piece fold-card" style="left:16px;top:14px;width:128px;height:132px">
  <div style="position:absolute;left:0;top:0;width:128px;height:62px;transform:rotate(180deg)">
    <div class="photo" role="img" aria-label="Photo of corporate business people" style="height:62px"></div>
    <div class="card-text" style="bottom:4px;font-size:6px;font-weight:700">Redundant IT &amp; Computer Equipment<br>Wanted – All UK Areas</div>
  </div>
  <svg class="wave" style="top:54px;bottom:auto" height="22" viewBox="0 0 128 22" preserveAspectRatio="none"><path d="M0 0H128V12Q64 26 0 10Z" fill="var(--green)"/></svg>
  <div class="brand" style="left:20px;top:92px;font-size:10px"><span class="brand-dot" style="width:10px;height:10px"></span>Cobalt Harvest</div>
  <svg class="wave" height="18" viewBox="0 0 128 18" preserveAspectRatio="none"><path d="M0 10Q64 -2 128 8V18H0Z" fill="var(--green)"/></svg>
</div>

<!-- director card: Rosalind -->
<div class="piece person-card" style="left:160px;top:14px;width:128px;height:132px">
  <div class="photo" role="img" aria-label="Photo of corporate business people" style="height:70px"></div>
  <svg class="wave" height="66" viewBox="0 0 128 66" preserveAspectRatio="none"><path d="M0 12Q64 -6 128 12V66H0Z" fill="var(--green)"/></svg>
  <div class="brand" style="left:20px;bottom:32px;font-size:9px;color:#fff"><span class="brand-dot" style="width:9px;height:9px"></span>Cobalt Harvest</div>
  <div class="card-text" style="bottom:9px;font-size:6px">Rosalind Pressey<br>Director</div>
</div>

<!-- company card -->
<div class="piece company-card" style="left:16px;top:156px;width:128px;height:100px">
  <div class="photo" role="img" aria-label="Photo of corporate business people" style="height:52px"></div>
  <svg class="wave" height="56" viewBox="0 0 128 56" preserveAspectRatio="none"><path d="M0 12Q64 -6 128 12V56H0Z" fill="var(--green)"/></svg>
  <div class="brand" style="left:20px;bottom:24px;font-size:9px;color:#fff"><span class="brand-dot" style="width:9px;height:9px"></span>Cobalt Harvest</div>
  <div class="card-text" style="bottom:8px;font-size:6px">Cobalt Harvest Ltd</div>
</div>

<!-- director card: Gordon -->
<div class="piece person-card" style="left:160px;top:156px;width:128px;height:100px">
  <div class="photo" role="img" aria-label="Photo of corporate business people" style="height:52px"></div>
  <svg class="wave" height="56" viewBox="0 0 128 56" preserveAspectRatio="none"><path d="M0 12Q64 -6 128 12V56H0Z" fill="var(--green)"/></svg>
  <div class="brand" style="left:20px;bottom:24px;font-size:9px;color:#fff"><span class="brand-dot" style="width:9px;height:9px"></span>Cobalt Harvest</div>
  <div class="card-text" style="bottom:8px;font-size:6px">Gordon Pressey – Director</div>
</div>

<!-- letterhead -->
<div class="piece letterhead" style="left:302px;top:14px;width:190px;height:232px">
  <div class="brand" style="left:12px;top:14px;font-size:9px"><span class="brand-dot" style="width:9px;height:9px"></span>Cobalt Harvest</div>
  <div class="address">14 Brindle Lane, Oakhurst Trading Park<br>Fenwick Cross, Herts HP9 3QL<br>gord@cobaltharvest-example.com</div>
  <div class="seal" style="left:50px;top:80px;width:90px;height:90px"></div>
  <svg class="wave" height="26" viewBox="0 0 190 26" preserveAspectRatio="none"><path d="M0 14Q95 -2 190 12V26H0Z" fill="var(--green)"/><path d="M0 9Q95 -7 190 7V12Q95 -2 0 14Z" fill="var(--green-light)"/></svg>
  <div class="footer-url">www.cobaltharvest-example.com</div>
</div>

<!-- fax -->
<div class="piece fax" style="left:512px;top:14px;width:190px;height:232px">
  <div class="brand" style="left:12px;top:14px;font-size:9px"><span class="brand-dot" style="width:9px;height:9px"></span>Cobalt Harvest</div>
  <div class="address">14 Brindle Lane, Oakhurst Trading Park<br>Fenwick Cross, Herts HP9 3QL<br>gord@cobaltharvest-example.com</div>
  <div class="doc-title" style="font-size:13px">FAX</div>
  <div style="position:absolute;left:14px;top:72px;width:162px">
    <div class="field"><span>To</span><i></i><span>From</span><i></i></div>
    <div class="field"><span>Fax</span><i></i><span>Date</span><i></i></div>
    <div class="field"><span>Pages</span><i></i><span>Re</span><i></i></div>
    <div><b class="fax-box"></b><b class="fax-box"></b><b class="fax-box"></b><b class="fax-box"></b></div>
  </div>
  <div class="seal" style="left:50px;top:118px;width:90px;height:90px"></div>
  <svg class="wave" height="26" viewBox="0 0 190 26" preserveAspectRatio="none"><path d="M0 14Q95 -2 190 12V26H0Z" fill="var(--green)"/><path d="M0 9Q95 -7 190 7V12Q95 -2 0 14Z" fill="var(--green-light)"/></svg>
  <div class="footer-url">www.cobaltharvest-example.com</div>
</div>

<!-- invoice -->
<div class="piece invoice" style="left:730px;top:14px;width:190px;height:232px">
  <div class="brand" style="left:12px;top:14px;font-size:9px"><span class="brand-dot" style="width:9px;height:9px"></span>Cobalt Harvest</div>
  <div class="address">14 Brindle Lane, Oakhurst Trading Park<br>Fenwick Cross, Herts HP9 3QL<br>gord@cobaltharvest-example.com</div>
  <div class="doc-title" style="font-size:11px">INVOICE</div>
  <div style="position:absolute;left:14px;top:70px;width:162px">
    <div class="field"><span>Invoice No</span><i></i><span>Date</span><i></i></div>
    <div class="field"><span>Account</span><i></i><span>Terms</span><i></i></div>
    <table style="margin-top:5px">
      <tr><th>Description</th><th>Qty</th><th>Price</th><th>Total</th></tr>
      <tr><td></td><td></td><td></td><td></td></tr>
      <tr><td></td><td></td><td></td><td></td></tr>
      <tr><td></td><td></td><td></td><td></td></tr>
      <tr><td></td><td></td><td>Subtotal</td><td></td></tr>
      <tr><td></td><td></td><td>VAT</td><td></td></tr>
      <tr><td></td><td></td><td>Total</td><td></td></tr>
    </table>
  </div>
  <div class="seal" style="left:55px;top:150px;width:80px;height:55px;border-radius:40px 40px 0 0"></div>
  <svg class="wave" height="26" viewBox="0 0 190 26" preserveAspectRatio="none"><path d="M0 14Q95 -2 190 12V26H0Z" fill="var(--green)"/><path d="M0 9Q95 -7 190 7V12Q95 -2 0 14Z" fill="var(--green-light)"/></svg>
  <div class="footer-url">www.cobaltharvest-example.com</div>
</div>

<!-- envelope -->
<div class="piece envelope" style="left:944px;top:40px;width:214px;height:134px">
  <svg style="position:absolute;left:0;top:0;display:block" width="214" height="50" viewBox="0 0 214 50" preserveAspectRatio="none"><path d="M0 0H214V24Q107 50 0 24Z" fill="var(--green)"/><path d="M0 19Q107 45 214 19V24Q107 50 0 24Z" fill="var(--green-light)"/></svg>
  <div class="brand" style="left:14px;top:70px;font-size:9px"><span class="brand-dot" style="width:9px;height:9px"></span>Cobalt Harvest</div>
  <svg class="wave" height="16" viewBox="0 0 214 16" preserveAspectRatio="none"><path d="M0 9Q107 -2 214 8V16H0Z" fill="var(--green)"/></svg>
</div>

<!-- business card stack -->
<div class="piece card-back" style="left:1020px;top:264px;width:128px;height:62px;transform:rotate(-6deg);background:var(--green)"></div>
<div class="piece card-front" style="left:1012px;top:274px;width:128px;height:62px;transform:rotate(-3deg)">
  <div class="brand" style="left:12px;top:14px;font-size:9px"><span class="brand-dot" style="width:9px;height:9px"></span>Cobalt Harvest</div>
  <div style="position:absolute;left:26px;top:28px;font-size:5px;color:var(--muted)">Gordon Pressey – Director</div>
  <svg class="wave" height="18" viewBox="0 0 128 18" preserveAspectRatio="none"><path d="M0 10Q64 -2 128 8V18H0Z" fill="var(--green)"/></svg>
</div>

</body>
</html>
```